Sleek business card design for digital agency.

Brief document attached for detailed description and inspiration. Looking for a minimalist sleek, cool, modern business card design.

Industry/Entity Type

Digital

```html
<!DOCTYPE html>
<html lang="en">
<head>
<meta charset="utf-8">
<title>Ferrow Labs – Business Card</title>
<link rel="stylesheet" href="https://fonts.googleapis.com/css2?family=Open+Sans:ital,wght@0,300;0,700;1,300&display=swap">
<style>
  :root {
    --card-bg: #000000;
    --ink: #ffffff;
  }
  html, body {
    margin: 0;
    padding: 0;
    overflow: hidden;
    background: var(--card-bg);
  }
  .card {
    position: relative;
    width: 686px;
    height: 1200px;
    background: var(--card-bg);
    color: var(--ink);
    font-family: "Open Sans", sans-serif;
    font-weight: 300;
    overflow: hidden;
  }
  .card__line {
    position: absolute;
    left: 0;
    width: 100%;
    height: 44px;
    line-height: 44px;
    text-align: center;
    font-size: 34px;
    white-space: nowrap;
  }
  .brand-mark {
    top: 441px;
    font-size: 30px;
    letter-spacing: 1px;
  }
  .person-name { top: 562px; font-weight: 700; font-size: 34px; }
  .person-role { top: 620px; font-style: italic; }
  .drink-order { top: 677px; }
  .address--street { top: 747px; }
  .address--city { top: 805px; }
  .phone--mobile { top: 875px; }
  .phone--office { top: 933px; }
  .contact--email { top: 1004px; }
  .contact--handle { top: 1061px; }
  .contact--social { top: 1118px; }
</style>
</head>
<body>
  <div class="card">
    <div class="card__line brand-mark">Ferrow Labs</div>

    <div class="card__line person-name">Daniel Hartley</div>
    <div class="card__line person-role">Marketing Director</div>
    <div class="card__line drink-order">Drink order: G&amp;T with cucumber</div>

    <div class="card__line address--street">Level 2, 18 Carrow Lane</div>
    <div class="card__line address--city">East Harbour NSW 2990</div>

    <div class="card__line phone--mobile">0400 555 218</div>
    <div class="card__line phone--office">02 5550 1847</div>

    <div class="card__line contact--email">dhartley@ferrowlabs.com</div>
    <div class="card__line contact--handle">@dhartley84</div>
    <div class="card__line contact--social">ferrowlabs.com/social</div>
  </div>
</body>
</html>
```